Buch-/E-Book-Cover für Kinderbuch gesucht
Zielgruppe
Wir sind gerade dabei ein Buch zum Thema 'Traumreisen für Kinder' zu erstellen und brauchen jetzt ein passendes Cover dazu. Die Zielgruppe besteht aus Eltern von Kindern ab ca. 4 Jahren. Bei den Traumreisen handelt es sich um Vorlesegeschichten für Kinder. Durch das Erzählen der Geschichten werden bildreiche Vorstellungen geweckt, mit deren Hilfe die Kinder in einen Zustand der Ruhe und Entspannung finden.
Aufgabenstellung
Titel, Untertitel und Autorenname müssen auf dem Cover stehen.
Der Titel des Buches lautet: Auf leisen Sternenpfaden über das Mondjahr: Ruhegeschichten für fröhliche Kinder zum Loslassen und Stärkung von Mut und Gelassenheit - inkl. Hörfassungen als kostenloser Download
Autor: Ulrike Benthof
Das Cover wird in 3 verschiedenen Versionen benötigt: Taschenbuch: 6 x 9 inch 2. Hardcover: 6 x 9 inch 3. EBook: 2,560 x 1,600 pixel.

```html
<!DOCTYPE html>
<html lang="de">
<head>
<meta charset="utf-8">
<title>Auf leisen Sternenpfaden über das Mondjahr – Cover</title>
<link href="https://fonts.googleapis.com/css2?family=Lato:wght@300;400&family=Permanent+Marker&display=swap" rel="stylesheet">
<style>
  :root {
    --stage: #cdebf5;
    --cover-base: #cfe6e1;
    --cover-light: #e4f2ef;
    --hill: #b9dbd3;
    --ink: #14323f;
    --badge: #f0d56a;
    --red: #e2504a;
    --salmon: #e8876a;
    --orange: #ef8a2a;
    --yellow: #f2c53d;
    --sage: #86b59a;
    --olive: #5f7f2e;
    --green: #3f7a3a;
    --teal: #0f4a56;
  }
  * { margin: 0; padding: 0; box-sizing: border-box; }
  html, body { width: 1200px; height: 620px; overflow: hidden; }
  body { background: var(--stage); display: flex; align-items: center; justify-content: center; }

  .cover {
    position: relative;
    width: 400px; height: 600px;
    background: var(--cover-base);
    overflow: hidden;
    font-family: "Lato", sans-serif;
    color: var(--ink);
  }
  .cover-waves { position: absolute; inset: 0; }

  .author {
    position: absolute; top: 30px; left: 0; right: 0;
    text-align: center; font-weight: 300; font-size: 14px; letter-spacing: .2px;
  }

  .title {
    position: absolute; top: 132px; left: 10px; right: 10px;
    text-align: center; font-family: "Permanent Marker", cursive;
    font-weight: 400; line-height: 1; white-space: nowrap;
  }
  .title-top { font-size: 22px; display: block; transform: rotate(-1deg); }
  .title-main { font-size: 38px; display: block; margin-top: 6px; letter-spacing: -.5px; }
  .title-bottom { font-size: 22px; display: block; margin-top: 8px; transform: rotate(-1deg); }
  .c1 { color: var(--red); } .c2 { color: var(--salmon); } .c3 { color: var(--orange); }
  .c4 { color: var(--yellow); } .c5 { color: var(--sage); } .c6 { color: var(--olive); }
  .c7 { color: var(--green); } .c8 { color: var(--teal); } .c9 { color: var(--ink); }

  .subtitle {
    position: absolute; top: 268px; left: 20px; right: 20px;
    text-align: center; font-size: 11px; font-weight: 400; line-height: 1.35;
  }

  .badge {
    position: absolute; left: 60px; top: 310px; width: 128px; height: 128px;
    border-radius: 50%; background: var(--badge);
    display: flex; align-items: center; justify-content: center; text-align: center;
    font-family: "Permanent Marker", cursive; font-weight: 400;
    font-size: 11px; line-height: 1.2; white-space: nowrap;
  }
  .badge span { transform: rotate(-9deg); display: block; }
  .curl-arrow { position: absolute; left: 196px; top: 300px; }

  .art { position: absolute; }
  .art-leaves-left { left: 0; top: 12px; width: 40px; height: 60px; background: linear-gradient(160deg, #4d8b35, #5f9d3e); border-radius: 0 60% 0 60%; }
  .art-leaves-right { right: 4px; top: 0; width: 44px; height: 100px; background: linear-gradient(180deg, #e8731f, #f29a3a); border-radius: 40% 10% 50% 50%; }
  .art-butterfly { left: 36px; top: 82px; width: 56px; height: 56px; background: var(--yellow); border-radius: 50% 50% 40% 40%; opacity: .9; }
  .art-oak-leaf { left: 300px; top: 88px; width: 44px; height: 40px; background: var(--orange); border-radius: 50% 10% 50% 40%; }
  .art-snowflakes { right: 8px; top: 340px; width: 100px; height: 90px; background: radial-gradient(circle, rgba(255,255,255,.85), rgba(255,255,255,0) 70%); }
  .art-flowers { left: 10px; top: 450px; width: 80px; height: 120px; border-radius: 40px; background: linear-gradient(180deg, #ef8a80 0%, #e2504a 50%, #f2c53d 100%); opacity: .9; }
  .art-reading-scene { left: 118px; top: 432px; width: 282px; height: 168px; background: linear-gradient(135deg, #8b5b3a 0%, #ef7f2a 40%, #4a8a37 72%, #e9c95a 100%); border-radius: 90px 40px 0 0; opacity: .92; }
</style>
</head>
<body>
  <main class="cover">
    <svg class="cover-waves" width="400" height="600" viewBox="0 0 400 600" aria-hidden="true">
      <path d="M0 0 H400 V70 C330 95 260 55 200 75 C140 95 80 70 0 55 Z" fill="var(--cover-light)"/>
      <path d="M0 520 C70 505 120 470 200 455 C280 440 340 470 400 450 V600 H0 Z" fill="var(--hill)"/>
    </svg>

    <div class="art art-leaves-left" role="img" aria-label="Grüne Blätter"></div>
    <div class="art art-leaves-right" role="img" aria-label="Orangefarbene Herbstblätter"></div>
    <div class="art art-butterfly" role="img" aria-label="Gelber Schmetterling"></div>
    <div class="art art-oak-leaf" role="img" aria-label="Herbstliches Eichenblatt"></div>

    <p class="author">Ulrike Benthof</p>

    <h1 class="title">
      <span class="title-top">AUF LEISEN</span>
      <span class="title-main"><span class="c1">S</span><span class="c2">T</span><span class="c3">E</span><span class="c4">R</span><span class="c3">N</span><span class="c2">E</span><span class="c5">N</span><span class="c5">P</span><span class="c6">F</span><span class="c7">A</span><span class="c8">D</span><span class="c9">E</span><span class="c9">N</span></span>
      <span class="title-bottom">ÜBER DAS MONDJAHR</span>
    </h1>

    <p class="subtitle">Ruhegeschichten für fröhliche Kinder zum Loslassen<br>und Stärkung von Mut und Gelassenheit</p>

    <div class="badge"><span>INKL.<br>HÖRFASSUNGEN<br>ALS<br>KOSTENLOSER<br>DOWNLOAD</span></div>

    <svg class="curl-arrow" width="40" height="54" viewBox="0 0 40 54" aria-hidden="true">
      <path d="M30 2 C34 18 26 30 16 28 C8 26 10 16 18 18 C26 20 22 40 6 46" fill="none" stroke="var(--ink)" stroke-width="2" stroke-linecap="round"/>
      <path d="M4 38 L5 47 L13 48" fill="none" stroke="var(--ink)" stroke-width="2" stroke-linecap="round" stroke-linejoin="round"/>
    </svg>

    <div class="art art-snowflakes" role="img" aria-label="Weiße Schneeflocken"></div>
    <div class="art art-flowers" role="img" aria-label="Bunte Blumen"></div>
    <div class="art art-reading-scene" role="img" aria-label="Mutter liest einem Kind im Bett aus einem grünen Buch vor"></div>
  </main>
</body>
</html>
```